Electrical panel service sticker w Bucket truck & Logo

We have a rather plain sticker we put on lighting panels to remind customers who to call for service. We want to redesign them with brushed aluminum background. We want a remake of the sticker with the outline of a bucket truck. You'll need to find or draw the outling of a bucket truck maybe with the boom up slightly as we will get these stickers die cut.

We want LOGO with Ph.# and Email.
Electrical * Lighting * Sign Service

Target Market(s)

Commercial property managers

Industry/Entity Type

Property Management

Requirements
Must have
• Bucket Truck Outline

```html
<!DOCTYPE html>
<html lang="en">
<head>
<meta charset="utf-8">
<title>Beacon Upkeep – Panel Service Sticker</title>
<link href="https://fonts.googleapis.com/css2?family=Montserrat:wght@500;600;700;800&display=swap" rel="stylesheet">
<style>
  :root {
    --page: #e9e6e1;
    --brand-red: #e3262b;
    --ink: #141414;
    --white: #ffffff;
    --steel-light: #f2f2f2;
    --steel-mid: #c9c9c9;
    --steel-dark: #a9a9a9;
    --band-top: #2e2e2e;
    --band-bottom: #101010;
    --truck-dark: #3a3a3a;
    --truck-soft: #8a8a8a;
  }
  * { box-sizing: border-box; margin: 0; padding: 0; }
  html, body {
    width: 1200px; height: 900px; overflow: hidden;
    background: var(--page);
    font-family: "Montserrat", sans-serif;
  }
  .sticker {
    position: absolute; left: 50px; top: 130px;
    width: 1100px; height: 641px;
    overflow: hidden;
    box-shadow: 0 4px 14px rgba(0,0,0,.25);
  }
  .sticker__steel {
    position: absolute; inset: 0 0 auto 0; height: 374px;
    background:
      repeating-linear-gradient(0deg, rgba(255,255,255,.18) 0 1px, rgba(0,0,0,.03) 1px 3px),
      linear-gradient(100deg, var(--steel-mid) 0%, var(--steel-light) 35%, var(--steel-dark) 60%, var(--steel-light) 85%, var(--steel-mid) 100%);
  }
  .sticker__band {
    position: absolute; left: 0; right: 0; bottom: 0; height: 267px;
    background:
      repeating-linear-gradient(0deg, rgba(255,255,255,.04) 0 1px, rgba(0,0,0,.05) 1px 3px),
      linear-gradient(180deg, var(--band-top), var(--band-bottom));
  }
  .brand-dot {
    position: absolute; left: 50px; top: 32px;
    width: 150px; height: 150px; border-radius: 50%;
    background: var(--brand-red);
  }
  .brand-name {
    position: absolute; left: 216px; top: 50px;
    color: var(--ink); font-weight: 800;
    font-size: 58px; line-height: 60px; letter-spacing: 2px;
  }
  .tagline {
    position: absolute; left: 217px; top: 168px;
    color: var(--brand-red); font-weight: 800;
    font-size: 14px; letter-spacing: 1.6px; white-space: nowrap;
  }
  .incorporated {
    position: absolute; left: 321px; top: 194px; width: 200px;
    text-align: center; color: var(--ink);
    font-weight: 500; font-size: 19px; letter-spacing: 2px;
  }
  .truck-art {
    position: absolute; left: 562px; top: 54px;
    width: 511px; height: 342px;
    background: linear-gradient(160deg, var(--truck-soft) 0%, var(--truck-dark) 100%);
    clip-path: polygon(30% 0, 100% 0, 100% 100%, 0 100%, 0 55%, 30% 55%);
  }
  .service-call {
    position: absolute; left: 74px; top: 310px;
    color: var(--ink); font-weight: 700; font-size: 40px; letter-spacing: .5px;
  }
  .contact {
    position: absolute; left: 62px;
    display: flex; align-items: center; gap: 22px;
  }
  .contact--phone { top: 434px; }
  .contact--email { top: 516px; }
  .contact__icon {
    width: 58px; height: 58px; border-radius: 50%;
    background: var(--brand-red);
    display: flex; align-items: center; justify-content: center;
    flex: none;
  }
  .contact__phone { color: var(--brand-red); font-weight: 700; font-size: 60px; line-height: 1; }
  .contact__email { color: var(--white); font-weight: 500; font-size: 56px; line-height: 1; }
</style>
</head>
<body>
  <main class="sticker">
    <div class="sticker__steel"></div>
    <div class="sticker__band"></div>

    <div class="brand-dot"></div>
    <h1 class="brand-name">BEACON<br>UPKEEP</h1>
    <p class="tagline">ELECTRICAL • LIGHTING • SIGN SERVICE</p>
    <p class="incorporated">INCORPORATED</p>

    <div class="truck-art" role="img" aria-label="Outline drawing of a bucket truck with its boom raised"></div>

    <p class="service-call">FOR SERVICE CALL</p>

    <div class="contact contact--phone">
      <span class="contact__icon">
        <svg width="32" height="32" viewBox="0 0 24 24" aria-hidden="true">
          <path fill="#fff" d="M3 9c0-2 3-4 9-4s9 2 9 4v1h-5V8.5c-1-.4-2.5-.6-4-.6s-3 .2-4 .6V10H3z"/>
          <path fill="#fff" d="M6 11h12l1 8H5z"/>
          <g fill="#e3262b"><circle cx="9.5" cy="14" r=".9"/><circle cx="12" cy="14" r=".9"/><circle cx="14.5" cy="14" r=".9"/><circle cx="9.5" cy="16.5" r=".9"/><circle cx="12" cy="16.5" r=".9"/><circle cx="14.5" cy="16.5" r=".9"/></g>
        </svg>
      </span>
      <span class="contact__phone">877-555-0142</span>
    </div>

    <div class="contact contact--email">
      <span class="contact__icon">
        <svg width="32" height="32" viewBox="0 0 24 24" aria-hidden="true">
          <rect x="3" y="6" width="18" height="12" rx="1" fill="#fff"/>
          <path d="M3.5 6.8 12 13l8.5-6.2M3.5 17.2 9.5 11.8M20.5 17.2l-6-5.4" fill="none" stroke="#e3262b" stroke-width="1.2"/>
        </svg>
      </span>
      <span class="contact__email">Service@beaconupkeep.com</span>
    </div>
  </main>
</body>
</html>
```